We have 'joined together' 6 micro-sites with a common theme. Looking to upgrade the design of a total of 26 pages on the abovementioned sites, whilst maintaining a common look and feel.

Goal is to improve customer experience and conversion rate, whilst maintaining Vantro rankings. New design to be responsive to different devices and SEO optimised

We prefer simple designs with the cleaness of Zelqo.com, however with more descriptive text. Target audience are business managers and owners, so site should convey professional capability, with a hint of playfulness. After all data can be fun? No?

See attached doc for further details.

Update: 19/8/2014. Following further consideration, the HTML coding no longer required. Once design is finalised, we require a PSD file for each page showing the full page layout, including all images and icons. We will extract the relevant bits from the PSD and do the coding and css inhouse.
Updates

Hi All The Pelquin Collective - PSD Design Only. HTML no longer required Following further consideration, the HTML / Css coding aspect of the project NO longer required. Once design is finalised, we require a PSD file from you for each of the 26 web pages, showing the page layout and including all images and icons. If one page layout is the same as another, then we request that you just supply images and icons for that page in a PSD file. We will then extract the relevant bits from the PSD and we will do the coding and css inhouse. Our main aim is to get an awesome, blow-your-sox-off design that compels users to convert. Many thanks in anticipation Oliver.

Project Deadline Extended
Reason: Changed deliverables from PSD, HTML and Coding t o PSD only. Hopefully this change will allow previous designers who were not interested to reconsider. Many thanks Oliver

Target Market(s)

Target market is business & IT managers within Australian organisations who are having problems with their data. Site must convey the impression that we are:
1) Very capable
2) Professional in our dealings
3) Reliable & trustworthy
4) Just a little bit quirky

Aprox. 60% of users are female, 40% male. Typically in the 30 to 55 year old bracket.

Number 1 requirements is that we don't embarrass our clients in any way.
2nd is that we do a good high quality job, delivering a good result.

We are not the cheapest nor the most expensive data shop around. We offer good value-for-money solutions. We are also reliable, friendly and available

Industry/Entity Type

Business

Font styles to use
Sans Serif

Requirements
Must have
• Simple yet information dense design. The "who we are" and "what we do" to be immediately visible above the fold. Images to be high quality. Good usability.
Simple navigation structure. Easy for users to find the info that they want.

In summary a simple, but good looking site, that compels users to contact us
Should not have
• No flash, fancy automation, rotating images, pop-ups etc.

```html
<!DOCTYPE html>
<html lang="en">
<head>
<meta charset="utf-8">
<title>The Pelquin Collective</title>
<link href="https://fonts.googleapis.com/css2?family=Lato:wght@300;400;700;900&display=swap" rel="stylesheet">
<style>
:root{
  --red:#e8453c;
  --red-dark:#c7342c;
  --navy:#2b3847;
  --navy-deep:#243040;
  --ink:#1f2b3a;
  --text:#555d66;
  --muted:#8a9099;
  --light:#f6f6f6;
  --white:#ffffff;
  --field:#3a4757;
}
*{box-sizing:border-box;margin:0;padding:0}
html,body{width:1200px;height:2301px;overflow:hidden;background:var(--white)}
body{font-family:'Lato',sans-serif;color:var(--text);position:relative}
.page{position:relative;width:1200px;height:2301px;overflow:hidden}
.abs{position:absolute}

/* hero */
.hero{left:0;top:0;width:1200px;height:743px;background:linear-gradient(180deg,#8b9a9b 0%,#7c8c8e 45%,#4a5862 80%,#2f3b46 100%)}
.hero-shade{left:0;top:0;width:1200px;height:743px;background:linear-gradient(180deg,rgba(0,0,0,0) 55%,rgba(20,28,38,.55) 100%)}
.nav{left:189px;top:20px;width:817px;height:55px;background:rgba(35,45,58,.92);display:flex;align-items:center}
.brand{width:162px;padding-left:24px;color:var(--white);font-weight:900;font-size:17px;letter-spacing:.2px}
.nav-item{height:55px;display:flex;align-items:center;padding:0 13px;color:var(--white);font-size:9px;font-weight:700;letter-spacing:.3px}
.nav-item.active{background:var(--red);padding:0 15px}
.nav-search{margin-left:auto;width:55px;height:55px;display:flex;align-items:center;justify-content:center;border-left:1px solid rgba(255,255,255,.1)}
.hero-kicker{left:189px;top:540px;color:var(--white);font-weight:900;font-size:44px;letter-spacing:-.5px}
.hero-title{left:189px;top:588px;color:var(--white);font-weight:900;font-size:66px;letter-spacing:-1.5px;line-height:1}

/* section heads */
.sec-head{display:flex;align-items:center;height:30px}
.sec-head h2{font-size:22px;font-weight:900;color:var(--ink);letter-spacing:-.2px}
.sec-head .bar{width:5px;height:30px;background:var(--red);margin:0 16px}
.sec-head span{font-size:15px;color:var(--text)}

/* who we are */
.who-head{left:191px;top:790px}
.who-lead{left:191px;top:836px;width:400px;font-size:19px;line-height:26px;color:var(--ink)}
.who-body{left:191px;top:965px;width:400px;font-size:9.5px;line-height:17px;color:var(--text)}
.btn{display:flex;align-items:center;height:47px;background:var(--red);color:var(--white);font-size:12px;font-weight:900}
.btn .arrow{width:47px;height:47px;background:var(--red-dark);display:flex;align-items:center;justify-content:center}
.know{left:191px;top:1054px;width:167px}
.know .label{padding-left:22px}
.what-head{left:614px;top:790px}
.service{width:200px}
.service .row{display:flex;align-items:center;gap:10px;height:40px}
.service h3{font-size:14px;font-weight:700;color:var(--ink)}
.service p{font-size:9.5px;line-height:17px;color:var(--muted);margin-top:2px}

/* benefits */
.benefits-bg{left:0;top:1134px;width:1200px;height:474px;background:var(--light)}
.benefits-card{left:177px;top:1134px;width:877px;height:378px;background:var(--white)}
.ben-head{left:191px;top:1160px}
.ben-lead{left:191px;top:1216px;width:400px;font-size:19px;line-height:25px;color:var(--ink)}
.ben-body{left:191px;top:1345px;width:400px;font-size:9.5px;line-height:17px;color:var(--text)}
.ben-photo{left:612px;top:1214px;width:399px;height:278px;background:linear-gradient(135deg,#e9ecef 0%,#c9cfd6 40%,#3d4654 75%,#222a34 100%)}
.dots{left:788px;top:1460px;display:flex;gap:6px}
.dots i{width:10px;height:10px;border-radius:50%;border:2px solid #333;display:block}
.dots i.on{background:var(--red);border-color:var(--red)}
.clients-tab{left:476px;top:1562px;width:404px;height:46px;background:var(--white);display:flex;align-items:center;padding-left:16px;font-size:20px;font-weight:900;color:var(--ink)}

/* testimonial */
.quote-band{left:0;top:1608px;width:1200px;height:155px;background:var(--navy)}
.quote-mark{left:193px;top:1656px;color:var(--red);font-size:70px;font-weight:900;line-height:1;font-style:normal}
.avatar{left:255px;top:1653px;width:70px;height:70px;background:linear-gradient(160deg,#d9d2cb,#8f8780)}
.quote-text{left:347px;top:1655px;width:640px;color:var(--white);font-size:18px;line-height:26px}
.quote-by{left:347px;top:1710px;color:#c9ced5;font-size:9px}
.red-rule{left:0;top:1761px;width:1200px;height:3px;background:var(--red)}

/* contact */
.contact{left:0;top:1764px;width:1200px;height:466px;background:linear-gradient(180deg,#34414f 0%,var(--navy) 35%,var(--navy-deep) 100%)}
.contact-item{width:260px;text-align:center;color:var(--white)}
.contact-item .icon{height:50px;display:flex;justify-content:center;align-items:flex-end}
.contact-item .val{margin-top:14px;font-size:16px}
.contact-item .val.small{font-size:11px}
.field{height:34px;border:1px solid #4a5767;padding:0 12px;display:flex;align-items:center;font-size:12px;color:#6d7886}
.field.focus{border:2px solid var(--red);color:var(--white)}
.message{left:191px;top:2008px;width:815px;height:86px;border:1px solid #4a5767;padding:12px;font-size:12px;color:#6d7886}
.send{left:511px;top:2151px;width:176px}
.send .label{padding-left:18px}

/* footer */
.footer{left:0;top:2230px;width:1200px;height:71px;background:var(--white)}
.copy{left:191px;top:2259px;font-size:10px;color:var(--muted)}
.social{left:612px;top:2258px;display:flex;gap:56px}
.social i{display:block;width:14px;height:14px;border-radius:50%;background:#b6bcc4}
.to-top{left:936px;top:2230px;width:70px;height:71px;background:#eceef0;display:flex;align-items:center;justify-content:center}
</style>
</head>
<body>
<div class="page">

  <section class="abs hero" role="img" aria-label="Photo of two children in suits wearing colander helmets and goggles, playing scientists at a desk"></section>
  <div class="abs hero-shade"></div>

  <nav class="abs nav">
    <div class="brand">PELQUIN COLLECTIVE</div>
    <div class="nav-item active">HOME</div>
    <div class="nav-item">DATA ANALYSIS</div>
    <div class="nav-item">DATA CLEANSING</div>
    <div class="nav-item">DATA MINING</div>
    <div class="nav-item">DATA SCRAPING</div>
    <div class="nav-item">DATA WAREHOUSES</div>
    <div class="nav-item">CONTACTS</div>
    <div class="nav-search">
      <svg width="14" height="14" viewBox="0 0 14 14"><circle cx="6" cy="6" r="4.5" fill="none" stroke="#8a95a3" stroke-width="1.6"/><line x1="9.3" y1="9.3" x2="13" y2="13" stroke="#8a95a3" stroke-width="1.6"/></svg>
    </div>
  </nav>

  <div class="abs hero-kicker">WELCOME TO</div>
  <h1 class="abs hero-title">THE PELQUIN COLLECTIVE</h1>

  <!-- who we are -->
  <div class="abs sec-head who-head"><h2>WHO WE ARE</h2><i class="bar"></i><span>Know About Us</span></div>
  <p class="abs who-lead">The Pelquin Collective is a Melbourne based business offering a comprehensive range of data services. We specialise in data analysis, data cleansing, data mining, data scraping and data warehouses.</p>
  <p class="abs who-body">Our goal is to help you extract value from your data in the form of pragmatic insights, trends and relationships. And then to analyse, interpret and use these findings in innovative ways that empower you to manage your organisation for greater profit, with improved decision-making and enhanced strategic, tactical and operational insight.</p>
  <div class="abs btn know">
    <span class="arrow"><svg width="10" height="12" viewBox="0 0 10 12"><path d="M3 1l5 5-5 5" fill="none" stroke="#fff" stroke-width="1.8"/></svg></span>
    <span class="label">KNOW MORE</span>
  </div>

  <!-- what we do -->
  <div class="abs sec-head what-head"><h2>WHAT WE DO</h2><i class="bar"></i><span>Know About Services</span></div>

  <div class="abs service" style="left:609px;top:835px">
    <div class="row"><svg width="40" height="40" viewBox="0 0 40 40"><rect x="4" y="24" width="5" height="12" fill="#e8453c"/><rect x="12" y="18" width="5" height="18" fill="#e8453c"/><rect x="20" y="22" width="5" height="14" fill="#e8453c"/><rect x="28" y="12" width="5" height="24" fill="#e8453c"/><path d="M4 18l9-7 8 5 12-11" fill="none" stroke="#e8453c" stroke-width="2"/></svg><h3>Data Analysis</h3></div>
    <p>Anim pariatur cliche reprehenderit, enim eiusmod high life accusamus terry cliche</p>
  </div>
  <div class="abs service" style="left:815px;top:835px">
    <div class="row"><svg width="40" height="40" viewBox="0 0 40 40"><line x1="30" y1="4" x2="18" y2="22" stroke="#e8453c" stroke-width="3"/><path d="M10 20l12 6-6 10-12-4z" fill="#e8453c"/></svg><h3>Data Cleansing</h3></div>
    <p>Anim pariatur cliche reprehenderit, enim eiusmod high life accusamus terry cliche</p>
  </div>
  <div class="abs service" style="left:609px;top:934px">
    <div class="row"><svg width="40" height="40" viewBox="0 0 40 40"><circle cx="16" cy="16" r="11" fill="none" stroke="#e8453c" stroke-width="2.5"/><line x1="24" y1="24" x2="35" y2="35" stroke="#e8453c" stroke-width="4"/><line x1="11" y1="16" x2="21" y2="16" stroke="#e8453c" stroke-width="2.5"/><line x1="16" y1="11" x2="16" y2="21" stroke="#e8453c" stroke-width="2.5"/></svg><h3>Data Mining</h3></div>
    <p>Anim pariatur cliche reprehenderit, enim eiusmod high life accusamus terry cliche</p>
  </div>
  <div class="abs service" style="left:815px;top:934px">
    <div class="row"><svg width="40" height="40" viewBox="0 0 40 40"><rect x="4" y="6" width="32" height="22" fill="none" stroke="#e8453c" stroke-width="2.5"/><rect x="16" y="28" width="8" height="4" fill="#e8453c"/><rect x="11" y="32" width="18" height="3" fill="#e8453c"/><circle cx="20" cy="17" r="4" fill="#e8453c"/></svg><h3>Data Scraping</h3></div>
    <p>Anim pariatur cliche reprehenderit, enim eiusmod high life accusamus terry cliche</p>
  </div>
  <div class="abs service" style="left:609px;top:1034px">
    <div class="row"><svg width="40" height="40" viewBox="0 0 40 40"><ellipse cx="20" cy="8" rx="14" ry="5" fill="#e8453c"/><path d="M6 12v6c0 3 6 5 14 5s14-2 14-5v-6c0 3-6 5-14 5S6 15 6 12z" fill="#e8453c"/><path d="M6 22v6c0 3 6 5 14 5s14-2 14-5v-6c0 3-6 5-14 5S6 25 6 22z" fill="#e8453c"/></svg><h3>Data Scraping</h3></div>
    <p>Anim pariatur cliche reprehenderit, enim eiusmod high life accusamus terry cliche</p>
  </div>
  <div class="abs service" style="left:815px;top:1034px">
    <div class="row"><svg width="40" height="40" viewBox="0 0 40 40"><rect x="14" y="4" width="20" height="24" fill="none" stroke="#e8453c" stroke-width="2.5"/><rect x="9" y="9" width="20" height="24" fill="#fff" stroke="#e8453c" stroke-width="2.5"/><rect x="4" y="14" width="20" height="24" fill="#fff" stroke="#e8453c" stroke-width="2.5"/></svg><h3>Data Resources</h3></div>
    <p>Anim pariatur cliche reprehenderit, enim eiusmod high life accusamus terry cliche</p>
  </div>

  <!-- benefits -->
  <div class="abs benefits-bg"></div>
  <div class="abs benefits-card"></div>
  <div class="abs sec-head ben-head"><h2>YOUR BENEFITS</h2><i class="bar"></i><span>Many Befits to Join Us</span></div>
  <p class="abs ben-lead">Our core speciality is solving business problems that require complex data analysis, cleansing, mining or modelling techniques. Your benefits include:</p>
  <p class="abs ben-body">Fast ROI: Quick access to skilled data professionals, without the overhead of building and maintaining your own infrastructure and team. Our fees are typically small in contrast to the additional profits or savings that our projects generate for our clients. Innovative practical solutions: We find smart ways to extract useful information from incomplete and disorganised data. We also have extensive industry experience AND the quantitative rigour to generate innovative yet pragmatic value-adding solutions. Connected to major universities. We have relationships with leading practitioners at major universities and business schools within Australia. This provides us with ready access to extensive expertise and the latest developments. We have never turned down a project due to it being too complex. Always confidential and discreet.</p>
  <div class="abs ben-photo" role="img" aria-label="Photo of business people shaking hands across a meeting table"></div>
  <div class="abs dots"><i></i><i></i><i class="on"></i></div>
  <div class="abs clients-tab">WE LOVE OUR &nbsp;CLIENTS</div>

  <!-- testimonial -->
  <div class="abs quote-band"></div>
  <div class="abs quote-mark">”</div>
  <div class="abs avatar" role="img" aria-label="Portrait photo of the client giving the testimonial"></div>
  <p class="abs quote-text">Thanks for the fast turnaround on our de-duplication project. ...I'm so impressed that I have already recommended you to two of our suppliers.</p>
  <p class="abs quote-by" style="top:1712px">Reid M/ Marketing Derictor</p>
  <div class="abs red-rule"></div>

  <!-- contact -->
  <section class="abs contact" role="img" aria-label="Faint city skyline backdrop in dark blue tones"></section>
  <div class="abs contact-item" style="left:190px;top:1810px">
    <div class="icon"><svg width="44" height="44" viewBox="0 0 44 44"><path d="M9 4l8 2 3 10-5 4c3 6 7 10 13 13l4-5 10 3 2 8c-2 3-5 4-8 4C19 41 3 25 4 11c0-3 2-6 5-7z" fill="#e8453c"/></svg></div>
    <div class="val">1300 555 014</div>
  </div>
  <div class="abs contact-item" style="left:468px;top:1810px">
    <div class="icon"><svg width="34" height="48" viewBox="0 0 34 48"><path d="M17 2C8 2 2 9 2 17c0 11 15 29 15 29s15-18 15-29C32 9 26 2 17 2z" fill="#e8453c"/><circle cx="17" cy="17" r="6" fill="#2b3847"/></svg></div>
    <div class="val small">1234 Street Name, City Name, India</div>
  </div>
  <div class="abs contact-item" style="left:748px;top:1810px">
    <div class="icon"><svg width="48" height="36" viewBox="0 0 48 36"><rect x="2" y="2" width="44" height="32" fill="#e8453c"/><path d="M2 4l22 16L46 4" fill="none" stroke="#2b3847" stroke-width="2.5"/></svg></div>
    <div class="val small">mail@pelquin-collective.com</div>
  </div>

  <div class="abs field focus" style="left:191px;top:1954px;width:257px">Name</div>
  <div class="abs field" style="left:470px;top:1954px;width:258px">Email</div>
  <div class="abs field" style="left:750px;top:1954px;width:256px">Phone</div>
  <div class="abs message">Message</div>
  <div class="abs btn send">
    <span class="arrow"><svg width="10" height="12" viewBox="0 0 10 12"><path d="M3 1l5 5-5 5" fill="none" stroke="#fff" stroke-width="1.8"/></svg></span>
    <span class="label">SEND MESSAGE</span>
  </div>

  <!-- footer -->
  <footer class="abs footer"></footer>
  <p class="abs copy">© Copyright 2014. All Rights Reserved</p>
  <div class="abs social"><i></i><i></i><i></i><i></i><i></i></div>
  <div class="abs to-top"><svg width="16" height="10" viewBox="0 0 16 10"><path d="M1 9l7-7 7 7" fill="none" stroke="#9aa1aa" stroke-width="1.8"/></svg></div>

</div>
</body>
</html>
```